Studying Effectively To Do List

I am looking to design a new "Study To Do List" for High School students (Ages 15 - 18) . This will be printed as an A4 notepad and so should only be a single A4 page.

The Design will need to be professional and look semi-serious but also be appealing to High school students (Ages 15 - 18) and should NOT be gender specific.

I have attached a word document outlining the structure of the page. The space provided should be large enough that people can write in it comfortably.

The notepad will most likely be printed in black and white but I'm also looking at coloured options - colours should be kept to a minimum.

This will be printed professionally and should also include a 3mm bleed.

The design should also include the business logo (included in the word document)

Target Market(s)

High School students (Ages 15 - 18). Both genders

Industry/Entity Type

Education

Font styles to use
Serif
Sans Serif

Requirements
Must have
• Please see the word document attached.
Should not have
• Too much colour

```html
<!DOCTYPE html>
<html lang="en">
<head>
<meta charset="utf-8">
<title>Study To Do List</title>
<link href="https://fonts.googleapis.com/css2?family=Archivo+Black&family=Open+Sans:wght@400;600;700&display=swap" rel="stylesheet">
<style>
  :root {
    --ink: #1b1b1b;
    --paper: #ffffff;
    --rule: #3a3a3a;
    --backdrop: #e9e6e1;
    --accent: #e8711f;
    --brand-navy: #1c3140;
  }
  * { margin: 0; padding: 0; box-sizing: border-box; }
  html, body { width: 1200px; height: 1200px; overflow: hidden; background: var(--backdrop); }
  body { position: relative; font-family: "Open Sans", Arial, sans-serif; color: var(--ink); }

  .sheet {
    position: absolute; left: 192px; top: 20px;
    width: 894px; height: 1270px;
    background: var(--paper);
    transform: scale(0.913); transform-origin: top left;
    box-shadow: 0 4px 14px rgba(0,0,0,.18);
  }
  .sheet > * { position: absolute; }

  .masthead {
    left: 0; top: 0; width: 894px; height: 70px; background: var(--ink);
    display: flex; align-items: center; justify-content: center;
  }
  .masthead h1 {
    font-family: "Archivo Black", Arial, sans-serif; font-weight: 400;
    color: var(--paper); font-size: 52px; letter-spacing: 2px; line-height: 1;
  }

  .section-title { font-weight: 700; font-size: 14px; left: 14px; }
  .date { left: 643px; top: 91px; font-size: 15px; display: flex; align-items: flex-end; }
  .date span { display: inline-block; width: 192px; border-bottom: 1px solid var(--ink); margin-left: 4px; height: 16px; }

  .grid-table { border: 1px solid var(--ink); border-collapse: collapse; }
  .grid-table td { border: 1px solid var(--ink); font-size: 18px; padding: 0 6px; vertical-align: middle; line-height: 1; }
  .revision { left: 16px; top: 124px; width: 862px; }
  .revision td { height: 29px; width: 50%; }

  .label { font-size: 12.5px; left: 14px; }
  .rule { height: 0; border-bottom: 1px solid var(--rule); }

  .notes-practice { left: 15px; top: 1052px; width: 715px; }
  .notes-practice th { border: 1px solid var(--ink); height: 35px; font-size: 14px; font-weight: 600; letter-spacing: .5px; }
  .notes-practice td { height: 34.5px; }

  .brand { left: 752px; top: 1160px; display: flex; align-items: center; gap: 8px; }
  .brand-dot { width: 22px; height: 22px; border-radius: 50%; background: var(--accent); }
  .brand-name { font-family: "Open Sans", Arial, sans-serif; font-weight: 700; font-size: 20px; color: var(--brand-navy); }
</style>
</head>
<body>
<main class="sheet">
  <header class="masthead"><h1>Study To Do List</h1></header>

  <div class="section-title" style="top:95px">REVISION</div>
  <div class="date">Date:<span></span></div>
  <table class="grid-table revision">
    <tr><td>❶</td><td>❺</td></tr>
    <tr><td>❷</td><td>❻</td></tr>
    <tr><td>❸</td><td>❼</td></tr>
    <tr><td>❹</td><td>❽</td></tr>
  </table>

  <div class="section-title" style="top:260px">HOMEWORK</div>
  <div class="label" style="top:296px">Subject:</div><div class="rule" style="left:16px;top:327px;width:865px"></div>
  <div class="label" style="top:330px">Task:</div><div class="rule" style="left:16px;top:361px;width:862px"></div>
  <div class="label" style="top:364px">Subject:</div><div class="rule" style="left:16px;top:395px;width:862px"></div>
  <div class="label" style="top:398px">Task:</div><div class="rule" style="left:16px;top:428px;width:865px"></div>
  <div class="label" style="top:431px">Subject:</div><div class="rule" style="left:16px;top:462px;width:865px"></div>
  <div class="label" style="top:465px">Task:</div><div class="rule" style="left:16px;top:496px;width:865px"></div>
  <div class="label" style="top:499px">Subject:</div><div class="rule" style="left:16px;top:530px;width:862px"></div>
  <div class="label" style="top:533px">Task:</div><div class="rule" style="left:16px;top:564px;width:865px"></div>
  <div class="label" style="top:567px">Subject:</div><div class="rule" style="left:16px;top:597px;width:865px"></div>
  <div class="label" style="top:600px">Task:</div><div class="rule" style="left:16px;top:631px;width:865px"></div>
  <div class="label" style="top:634px">Subject:</div><div class="rule" style="left:16px;top:665px;width:865px"></div>
  <div class="label" style="top:668px">Task:</div><div class="rule" style="left:14px;top:698px;width:864px"></div>

  <div class="section-title" style="top:718px;font-size:12.5px">ASSESSMENTS</div>
  <div class="label" style="top:735px">Assessment:</div><div class="rule" style="left:16px;top:766px;width:426px"></div>
  <div class="label" style="top:769px">Due</div><div class="rule" style="left:38px;top:783px;width:403px"></div>
  <div class="label" style="top:786px">Element:</div><div class="rule" style="left:16px;top:817px;width:865px"></div>
  <div class="label" style="top:819px">Assessment:</div><div class="rule" style="left:16px;top:850px;width:426px"></div>
  <div class="label" style="top:853px">Due</div><div class="rule" style="left:38px;top:867px;width:403px"></div>
  <div class="label" style="top:870px">Element:</div><div class="rule" style="left:16px;top:901px;width:865px"></div>

  <div class="label" style="top:904px">Assessment :</div><div class="rule" style="left:90px;top:918px;width:246px"></div>
  <div class="label" style="left:346px;top:904px">Due</div><div class="rule" style="left:368px;top:918px;width:310px"></div>
  <div class="label" style="top:921px">Element&nbsp;&nbsp;&nbsp;&nbsp;&nbsp;&nbsp;:</div><div class="rule" style="left:90px;top:935px;width:588px"></div>
  <div class="label" style="top:938px">Assessment :</div><div class="rule" style="left:90px;top:952px;width:246px"></div>
  <div class="label" style="left:346px;top:938px">Due</div><div class="rule" style="left:368px;top:952px;width:310px"></div>
  <div class="label" style="top:955px">Element&nbsp;&nbsp;&nbsp;&nbsp;&nbsp;&nbsp;:</div><div class="rule" style="left:90px;top:969px;width:588px"></div>
  <div class="label" style="top:972px">Assessment :</div><div class="rule" style="left:90px;top:986px;width:246px"></div>
  <div class="label" style="left:346px;top:972px">Due</div><div class="rule" style="left:368px;top:986px;width:310px"></div>
  <div class="label" style="top:989px">Element&nbsp;&nbsp;&nbsp;&nbsp;&nbsp;&nbsp;:</div><div class="rule" style="left:90px;top:1003px;width:588px"></div>
  <div class="label" style="top:1006px">Assessment :</div><div class="rule" style="left:90px;top:1020px;width:246px"></div>
  <div class="label" style="left:346px;top:1006px">Due</div><div class="rule" style="left:368px;top:1020px;width:310px"></div>
  <div class="label" style="top:1023px">Element&nbsp;&nbsp;&nbsp;&nbsp;&nbsp;&nbsp;:</div><div class="rule" style="left:86px;top:1037px;width:590px"></div>

  <table class="grid-table notes-practice">
    <tr><th colspan="2" style="width:351px">NOTES</th><th>PRACTICE</th></tr>
    <tr><td style="width:174px">❶</td><td style="width:177px">❺</td><td></td></tr>
    <tr><td>❷</td><td>❻</td><td></td></tr>
    <tr><td>❸</td><td>❼</td><td></td></tr>
    <tr><td>❹</td><td>❽</td><td></td></tr>
  </table>

  <div class="brand"><span class="brand-dot"></span><span class="brand-name">Quorvane</span></div>
</main>
</body>
</html>
```